brightleafwell.com and torvahealth.com

I'd like to do a web design re-make on two of our websites. Brightleafwell.com is focused on selling nutriceutical products (private labeled by brightleafwell.com), and provide an expert blog to give great advices on general health.

Torvahealth.com is a site for Dr. Moreau's new medicine clinic. It should be integrated with brightleafwell.com. Clients can directly make appointments on the site, and order products from brightleafwell.com.

Target Market(s)

Middle to upper

Industry/Entity Type

Clinic

Number of Pages Required

4 page

Font styles to use
Serif
Sans Serif

Colors
0254a3
0792cd
33a6d7
00a98f
33b7a4
acd036
9bcb3c
cadf82

Requirements
Must have
• Home page tabs: About Dr. Moreau, Store, Blog, Videos, Appointment
• Home page content should include: a promotional section (with moving features), an appointment book (for online appointment booking), a product section (for store), and a blog section.
Nice to have
• The look and feel should be modern, professional, trustworthy, zen.
Should not have
• Real pictures of people, except for Dr. Moreau.

```html
<!DOCTYPE html>
<html lang="en">
<head>
<meta charset="utf-8">
<title>Brightleaf Well – Empowering Your Ageless Body and Mind</title>
<link rel="stylesheet" href="https://fonts.googleapis.com/css2?family=Roboto:wght@100;300;400;500;700&display=swap">
<style>
:root{
  --brand:#0254a3;
  --brand-dark:#0a3f85;
  --sky:#33a6d7;
  --band:#3f6fc0;
  --ink:#2b2b2b;
  --muted:#6b6f78;
  --paper:#ffffff;
  --mist:#eef3fb;
  --footer:#0d1b35;
  --line:#c8d3e6;
}
*{box-sizing:border-box;margin:0;padding:0}
html,body{width:1200px;height:3103px;overflow:hidden}
body{font-family:"Roboto",Arial,sans-serif;color:var(--ink);background:var(--paper);position:relative}
.abs{position:absolute}

/* header */
.site-header{left:0;top:0;width:1200px;height:130px;background:var(--paper)}
.brand-name{left:52px;top:30px;font-size:40px;font-weight:700;color:var(--brand);line-height:1;display:flex;align-items:center;gap:12px}
.brand-name .mark{width:26px;height:26px;background:var(--sky);border-radius:50%}
.search{left:698px;top:26px;width:254px;height:32px;border:1px solid var(--line);border-radius:3px}
.search svg{position:absolute;right:8px;top:7px}
.login{left:972px;top:24px;width:132px;height:36px;background:var(--brand);color:#fff;font-size:14px;font-weight:500;display:flex;align-items:center;justify-content:center;border-radius:3px}
.main-nav{left:315px;top:72px;display:flex;font-size:13px;text-transform:uppercase;color:#333}
.main-nav a{color:inherit;text-decoration:none;display:block;padding:10px 0;margin-right:42px}
.main-nav a.active{border:2px solid var(--sky);color:var(--brand);border-radius:3px;padding:9px 24px}

/* hero */
.hero{left:0;top:130px;width:1200px;height:582px;background:linear-gradient(100deg,#d9c3b6 0%,#ead8cd 30%,#f2ede9 55%,#f7f7f8 100%)}
.hero-title{left:640px;top:190px;text-align:right;width:460px;color:var(--brand);font-weight:100;line-height:1.05}
.hero-title .l1{font-size:78px;font-weight:100}
.hero-title .l2{font-size:46px;font-weight:300;color:var(--sky)}
.hero-title .l3{font-size:78px;font-weight:100}
.hero-title .and{font-size:50px;color:var(--sky)}
.slider-dots{left:920px;top:584px;display:flex;gap:8px}
.slider-dots span{width:18px;height:18px;border-radius:50%;background:var(--brand)}
.slider-dots span.on{background:#fff;border:4px solid var(--brand)}

/* appointment */
.booking{left:171px;top:641px;width:864px;height:96px;background:#fff;box-shadow:0 8px 16px rgba(0,0,0,.15);display:flex;align-items:center;padding:0 28px;gap:26px}
.booking h3{font-size:17px;font-weight:700;text-transform:uppercase;color:#222;width:230px}
.field{width:212px;height:38px;border:1px solid var(--line);font-size:11px;color:#444;display:flex;align-items:center;justify-content:space-between;padding:0 10px}
.booking .next{width:116px;height:40px;background:var(--brand);color:#fff;font-size:12px;font-weight:500;display:flex;align-items:center;justify-content:center;border-radius:3px}

/* about */
.about-photo{left:134px;top:827px;width:156px;height:156px;border-radius:50%;background:linear-gradient(160deg,#6c5a52,#cfb3a1);border:6px solid #fff;box-shadow:0 2px 6px rgba(0,0,0,.3)}
.about-title{left:336px;top:762px;font-size:30px;font-weight:400;color:#222}
.about-title span{color:var(--brand)}
.about-text{left:336px;top:818px;width:760px;font-size:13px;line-height:1.75;color:#333}
.about-text p{margin-bottom:12px}
.read-more{left:983px;top:975px;width:116px;height:34px;background:var(--brand);color:#fff;font-size:13px;display:flex;align-items:center;justify-content:center;gap:8px;border-radius:3px}

/* values band */
.values{left:0;top:1073px;width:1200px;height:414px;background:linear-gradient(180deg,#4775c6,#3a66b7)}
.value{width:270px;text-align:center;color:#fff}
.value h4{font-size:22px;font-weight:700;line-height:1.15;height:60px;text-transform:uppercase}
.value .icon{width:104px;height:104px;border:3px solid #dfe9ff;border-radius:22px 4px 22px 4px;margin:16px auto 24px;display:flex;align-items:center;justify-content:center}
.value p{font-size:11px;font-weight:700;line-height:1.45;text-transform:uppercase}

/* products */
.products{left:0;top:1487px;width:1200px;height:1073px;background:var(--mist)}
.products-title{left:0;top:1530px;width:1200px;text-align:center;font-size:32px;color:var(--brand);font-weight:400}
.rule{top:1552px;width:330px;border-top:2px dashed #9aa7bd}
.card{width:234px;height:388px;background:#fff;box-shadow:0 6px 10px rgba(0,0,0,.12);text-align:center}
.card.featured{background:var(--brand);color:#fff}
.tag{position:absolute;right:0;top:0;width:48px;height:22px;background:var(--brand);color:#fff;font-size:11px;font-weight:500;display:flex;align-items:center;justify-content:center}
.featured .tag{background:#fff;color:var(--brand)}
.bottle{position:absolute;left:62px;top:34px;width:110px;height:150px;border-radius:18px 18px 10px 10px;background:linear-gradient(90deg,#c9ced6,#ffffff 45%,#d2d6dc)}
.card .price{position:absolute;left:0;width:100%;top:210px;font-size:28px;font-weight:700;color:var(--brand)}
.featured .price{color:#fff}
.card .name{position:absolute;left:0;width:100%;top:252px;font-size:15px;font-weight:700;text-transform:uppercase;white-space:nowrap}
.card .meta{position:absolute;left:0;width:100%;top:276px;font-size:12px;line-height:1.5;color:#444}
.featured .meta{color:#e8eefa}
.card .cart{position:absolute;left:50%;margin-left:-67px;top:326px;width:134px;height:44px;background:var(--brand);color:#fff;font-size:13px;display:flex;align-items:center;justify-content:center}
.featured .cart{background:#fff;color:var(--brand)}
.pager{left:833px;top:2460px;display:flex;gap:14px}
.pager span{width:46px;height:46px;border-radius:50%;background:#fff;box-shadow:0 2px 5px rgba(0,0,0,.2);display:flex;align-items:center;justify-content:center;font-size:16px;color:#333}

/* blog */
.blog-title{left:132px;top:2600px;font-size:28px;font-weight:700;color:var(--brand)}
.blog-arrow{width:28px;height:28px;border-radius:50%;background:var(--brand);display:flex;align-items:center;justify-content:center}
.post{width:290px;text-align:center}
.post .photo{width:156px;height:156px;margin:0 auto;border-radius:50%;border:6px solid #fff;box-shadow:0 2px 6px rgba(0,0,0,.3)}
.post .author{margin-top:14px;font-size:16px;color:#333}
.post .stats{margin-top:8px;display:flex;justify-content:center;gap:24px;font-size:12px;color:#444;align-items:center}
.post .stats span{display:flex;align-items:center;gap:6px}
.post .excerpt{margin-top:10px;font-size:13px;color:var(--sky);text-transform:uppercase;line-height:1.4}
.related{left:789px;top:2712px;width:328px;font-size:26px;font-weight:400;color:#333;text-align:center}
.related span{color:var(--brand)}
.video{left:796px;top:2764px;width:316px;height:188px;background:linear-gradient(120deg,#1b1b1d,#5a5a5e 60%,#2a2a2c)}
.video .play{position:absolute;left:128px;top:64px;width:60px;height:60px;border-radius:50%;background:rgba(255,255,255,.35)}
.video-caption{left:796px;top:2970px;width:316px;display:flex;justify-content:space-between;font-size:13px;color:#333}

/* footer */
.site-footer{left:0;top:3020px;width:1200px;height:83px;background:var(--footer);color:#fff}
.site-footer .addr{left:94px;top:20px;font-size:12px;line-height:1.5;color:#dfe5f0}
.site-footer .phone{left:344px;top:28px;font-size:24px;font-weight:700}
.site-footer .mail{left:650px;top:32px;font-size:15px;color:#dfe5f0}
.socials{left:884px;top:12px;display:flex;gap:10px}
.socials span{width:38px;height:38px;border:2px solid #fff;border-radius:50%}
.copy{left:846px;top:62px;font-size:9px;color:#b8c2d6}
</style>
</head>
<body>

<header class="site-header abs">
  <div class="brand-name abs"><span class="mark"></span>Brightleaf Well</div>
  <div class="search abs"><svg width="16" height="16" viewBox="0 0 16 16"><circle cx="6.5" cy="6.5" r="4.5" fill="none" stroke="#0254a3" stroke-width="2"/><path d="M10 10l4 4" stroke="#0254a3" stroke-width="2"/></svg></div>
  <div class="login abs">LOGIN</div>
  <nav class="main-nav abs">
    <a class="active">Home</a><a>About Dr. Moreau</a><a>Store</a><a>Blog</a><a>Videos</a><a>Appointment</a><a>Contact Us</a>
  </nav>
</header>

<section class="hero abs" role="img" aria-label="Portrait of a woman with closed eyes and smooth skin, soft light background"></section>
<div class="hero-title abs">
  <div class="l1">Empowering</div>
  <div class="l2">Your Ageless</div>
  <div class="l3">Body <span class="and">and</span> Mind</div>
</div>
<div class="slider-dots abs"><span class="on"></span><span></span><span></span></div>

<form class="booking abs">
  <h3>Make an appointment</h3>
  <div class="field">Appointment Date
    <svg width="14" height="14" viewBox="0 0 14 14"><rect x="1" y="2" width="12" height="11" fill="none" stroke="#0254a3" stroke-width="1.5"/><path d="M1 5h12M4 0v3M10 0v3" stroke="#0254a3" stroke-width="1.5"/></svg></div>
  <div class="field">Appointment Time
    <svg width="14" height="14" viewBox="0 0 14 14"><circle cx="7" cy="7.5" r="5.5" fill="none" stroke="#0254a3" stroke-width="1.5"/><path d="M7 4.5v3h2.5" stroke="#0254a3" stroke-width="1.5" fill="none"/></svg></div>
  <div class="next">Next Steps</div>
</form>

<section class="about">
  <div class="about-photo abs" role="img" aria-label="Portrait of Dr. Moreau"></div>
  <h2 class="about-title abs">About <span>Dr.Moreau</span></h2>
  <div class="about-text abs">
    <p>Dr. Elise Moreau, as thousands of patients refer to as "Dr. Moreau" or "the Healer", brings a great combination between modern medical sciences and ancient medicine. Every smile, hug and encouraging word from her in addition to her sincerely caring and loving nature give those in need tremendous healing power!</p>
    <p>Here's a brief introduction for Dr. Elise Moreau's background:</p>
    <p style="margin-bottom:0">M.D. from Northgate University, Clinical Medicine<br>M.S. from Harbor State University, Medical Human Physiology</p>
  </div>
  <div class="read-more abs">Read more
    <svg width="16" height="16" viewBox="0 0 16 16"><circle cx="8" cy="8" r="7" fill="none" stroke="#fff" stroke-width="1.3"/><path d="M5 8h6M8.5 5.5L11 8l-2.5 2.5" stroke="#fff" stroke-width="1.3" fill="none"/></svg></div>
</section>

<section class="values abs">
  <div class="value abs" style="left:186px;top:70px">
    <h4>High<br>Quality</h4>
    <div class="icon"><svg width="52" height="52" viewBox="0 0 52 52"><rect x="6" y="10" width="34" height="34" fill="none" stroke="#fff" stroke-width="4"/><path d="M14 26l9 9 22-24" stroke="#fff" stroke-width="5" fill="none"/></svg></div>
    <p>Only the highest quality and<br>purest nutraceuticals.</p>
  </div>
  <div class="value abs" style="left:468px;top:70px">
    <h4>GMP<br>Certified</h4>
    <div class="icon"><svg width="52" height="52" viewBox="0 0 52 52"><circle cx="26" cy="20" r="13" fill="none" stroke="#fff" stroke-width="4"/><circle cx="26" cy="20" r="6" fill="#fff"/><path d="M18 31l-5 16 7-4 4 6 2-14M34 31l5 16-7-4-4 6-2-14" fill="none" stroke="#fff" stroke-width="3"/></svg></div>
    <p>Meets or exceeds all policies and<br>principles as outlined by the<br>current good manufacturing<br>practices (CGMPs).</p>
  </div>
  <div class="value abs" style="left:752px;top:70px">
    <h4>Pharmaceutical<br>Grade</h4>
    <div class="icon"><svg width="54" height="50" viewBox="0 0 54 50"><rect x="3" y="12" width="48" height="34" rx="4" fill="#fff"/><path d="M19 12V5h16v7" fill="none" stroke="#fff" stroke-width="4"/><path d="M27 20v18M18 29h18" stroke="#3f6fc0" stroke-width="6"/></svg></div>
    <p>Only the most evidence-based,<br>pharmaceutical-grade raw materials.</p>
  </div>
</section>

<section class="products abs"></section>
<div class="rule abs" style="left:160px"></div>
<div class="rule abs" style="left:710px"></div>
<h2 class="products-title abs">PRODUCTS</h2>

<div class="card featured abs" style="left:122px;top:1629px"><span class="tag">NEW</span><div class="bottle" role="img" aria-label="White supplement bottle"></div><div class="price">$60.00</div><div class="name">Adrenavita</div><div class="meta">SKU: BLW-0100<br>120 Capsules</div><div class="cart">ADD TO CART</div></div>
<div class="card abs" style="left:370px;top:1629px"><span class="tag">SALE</span><div class="bottle" role="img" aria-label="White supplement bottle"></div><div class="price">$35.00</div><div class="name">Pollen Calm</div><div class="meta">SKU: BLW0200<br>60 Capsules</div><div class="cart">ADD TO CART</div></div>
<div class="card abs" style="left:618px;top:1629px"><span class="tag">SALE</span><div class="bottle" role="img" aria-label="White supplement bottle"></div><div class="price">$60.00</div><div class="name">Core Harmony</div><div class="meta">SKU: BLW0300<br>120 Capsules</div><div class="cart">ADD TO CART</div></div>
<div class="card abs" style="left:864px;top:1629px"><span class="tag">SALE</span><div class="bottle" role="img" aria-label="White supplement bottle"></div><div class="price">$35.00</div><div class="name">B Plex Plus</div><div class="meta">SKU: BLW0400<br>60 Capsules</div><div class="cart">ADD TO CART</div></div>

<div class="card abs" style="left:122px;top:2030px"><span class="tag">SALE</span><div class="bottle" role="img" aria-label="White supplement bottle"></div><div class="price">$40.00</div><div class="name">Radiant Skin</div><div class="meta">SKU: BLW0500<br>120 Capsules</div><div class="cart">ADD TO CART</div></div>
<div class="card abs" style="left:370px;top:2030px"><span class="tag">SALE</span><div class="bottle" role="img" aria-label="White supplement bottle"></div><div class="price">$40.00</div><div class="name">Candibalance</div><div class="meta">SKU: BLW0700<br>60 Capsules</div><div class="cart">ADD TO CART</div></div>
<div class="card abs" style="left:618px;top:2030px"><span class="tag">SALE</span><div class="bottle" role="img" aria-label="White supplement bottle"></div><div class="price">$50.00</div><div class="name" style="font-size:14px">Heart Vitality Formula</div><div class="meta">SKU: BLW0800<br>60 Capsules</div><div class="cart">ADD TO CART</div></div>
<div class="card abs" style="left:864px;top:2030px"><span class="tag">SALE</span><div class="bottle" role="img" aria-label="White supplement bottle"></div><div class="price">$30.00</div><div class="name">Open Breath</div><div class="meta">SKU: BLW0900<br>60 Capsules</div><div class="cart">ADD TO CART</div></div>

<div class="pager abs"><span>&laquo;</span><span>1</span><span>2</span><span>3</span><span>&raquo;</span></div>

<section class="blog">
  <h2 class="blog-title abs">BLOG</h2>
  <div class="blog-arrow abs" style="left:84px;top:2816px"><svg width="10" height="12" viewBox="0 0 10 12"><path d="M8 1L2 6l6 5" stroke="#fff" stroke-width="2" fill="none"/></svg></div>
  <div class="blog-arrow abs" style="left:708px;top:2816px"><svg width="10" height="12" viewBox="0 0 10 12"><path d="M2 1l6 5-6 5" stroke="#fff" stroke-width="2" fill="none"/></svg></div>

  <article class="post abs" style="left:139px;top:2676px">
    <div class="photo" role="img" aria-label="Portrait of blog author" style="background:linear-gradient(160deg,#c89a6a,#efe2d4)"></div>
    <div class="author">Nora Lind</div>
    <div class="stats"><span><svg width="16" height="16" viewBox="0 0 16 16"><circle cx="8" cy="9" r="6" fill="none" stroke="#0254a3" stroke-width="1.6"/><path d="M8 6v3h2" stroke="#0254a3" stroke-width="1.6" fill="none"/></svg>12/2014</span><span><svg width="16" height="14" viewBox="0 0 16 14"><path d="M1 1h14v9H6l-3 3v-3H1z" fill="none" stroke="#0254a3" stroke-width="1.6"/></svg>04</span></div>
    <div class="excerpt">Oque penatibus et magnis<br>dis parturient</div>
  </article>
  <article class="post abs" style="left:434px;top:2676px">
    <div class="photo" role="img" aria-label="Portrait of blog author" style="background:linear-gradient(160deg,#5a3c2c,#d9c2ae)"></div>
    <div class="author">Kara Wynn</div>
    <div class="stats"><span><svg width="16" height="16" viewBox="0 0 16 16"><circle cx="8" cy="9" r="6" fill="none" stroke="#0254a3" stroke-width="1.6"/><path d="M8 6v3h2" stroke="#0254a3" stroke-width="1.6" fill="none"/></svg>12/2014</span><span><svg width="16" height="14" viewBox="0 0 16 14"><path d="M1 1h14v9H6l-3 3v-3H1z" fill="none" stroke="#0254a3" stroke-width="1.6"/></svg>05</span></div>
    <div class="excerpt">Oque penatibus et magnis<br>dis parturient</div>
  </article>

  <h3 class="related abs">Related <span>Video</span></h3>
  <div class="video abs" role="img" aria-label="Video still of a face treatment with steam"><div class="play"></div>
    <svg class="abs" style="left:150px;top:80px" width="22" height="28" viewBox="0 0 22 28"><path d="M2 2l18 12L2 26z" fill="#fff"/></svg></div>
  <div class="video-caption abs"><span>&lt;</span><span>" About face treatment"</span><span>&gt;</span></div>
</section>

<footer class="site-footer abs">
  <svg class="abs" style="left:62px;top:22px" width="18" height="26" viewBox="0 0 18 26"><path d="M9 1a8 8 0 0 0-8 8c0 6 8 16 8 16s8-10 8-16a8 8 0 0 0-8-8z" fill="#fff"/><circle cx="9" cy="9" r="3" fill="#0d1b35"/></svg>
  <div class="addr abs">1480 Harbor View Rd, Suite C<br>Bayside, CA</div>
  <svg class="abs" style="left:312px;top:28px" width="22" height="26" viewBox="0 0 22 26"><rect x="4" y="1" width="14" height="24" rx="3" fill="#fff"/><rect x="6" y="4" width="10" height="15" fill="#0d1b35"/></svg>
  <div class="phone abs">555 - 014 - 0666</div>
  <svg class="abs" style="left:614px;top:32px" width="24" height="18" viewBox="0 0 24 18"><rect x="1" y="1" width="22" height="16" fill="none" stroke="#fff" stroke-width="1.6"/><path d="M1 1l11 9 11-9" fill="none" stroke="#fff" stroke-width="1.6"/></svg>
  <div class="mail abs">torvahealthinc@mailhub.com</div>
  <div class="socials abs"><span></span><span></span><span></span><span></span></div>
  <div class="copy abs">© Copyright 2014 by Brightleafwell.com All Rights Reserved.</div>
</footer>

</body>
</html>
```